Music portal needs a sleek mobile app design

We need an innovative, cutting edge design for our mobile app for www.loftaroundsound.com . LOFTAROUND Music is a platform that lets independent musicians upload and share their music for free. Music lovers can discover new music too.

If you visit the website, you'll get an idea of our brand colors and theme. im attaching the logo and our new discover page layout. We use "din Next LT pro" as our brand font.

We are looking for an app optimized for iOS, but can be used on Android and windows too.

Im looking for a design that flows and navigates with user intuition and is sleek, flat style in nature and has Similar apps are tunewharf, riffpantry and beatorchard.

Here are some ideas we like, but please dont copy. Come up with something similar in 'feel'

https://www.portfoliarc.net/gallery/B-TUNE-IT-Music-application/4412983

https://sketchvault.com/shots/2290518-Music-App

The most important pages/ screens for us are:
- The discover screen
- The login and sign up screens
- The splash screen
- The track player screen
- The use profile page screen
Updates

It seems no design has come close to what I was looking for so I will be requesting a refund and withdrawing this project. Thanks for your effort

Target Market(s)

music, music app, tunewharf, loftaround music, music app design

Colors
f78f20
ffcf3e
ffffff
000000

Requirements
Must have
• a sleek easy to use navigation- please create an account on loftaroundsound.com to see how the site works.
Nice to have
• Sleek screen to screen transitions
Should not have
• no 3d designs. Flat design only

```html
<!DOCTYPE html>
<html lang="en">
<head>
<meta charset="utf-8">
<title>LOFTAROUND Music – Profile</title>
<link href="https://fonts.googleapis.com/css2?family=Barlow:wght@400;500;600&display=swap" rel="stylesheet">
<style>
  :root{
    --orange:#f78f20;
    --yellow:#ffcf3e;
    --white:#ffffff;
    --black:#000000;
    --bar:#1c1c1c;
    --band:#2a2a2a;
    --stage:#b9c1c4;
    --grid-bg:#a3a3a3;
    --panel-top:#d9d9d9;
    --panel-bottom:#f2f2f2;
    --muted:#cfcfcf;
  }
  *{box-sizing:border-box;margin:0;padding:0}
  html,body{width:1200px;height:900px;overflow:hidden}
  body{background:var(--stage);font-family:"Barlow",Arial,sans-serif;position:relative}
  .screen{position:absolute;left:393px;top:82px;width:414px;height:736px;background:var(--grid-bg);overflow:hidden;box-shadow:0 12px 40px rgba(0,0,0,.18)}
  .status-bar{height:20px;background:var(--black);color:var(--white);font-size:11px;font-weight:500;display:flex;align-items:center;justify-content:space-between;padding:0 8px}
  .status-left{display:flex;align-items:center;gap:4px}
  .battery{display:flex;align-items:center;gap:4px}
  .battery-shape{width:22px;height:10px;border:1px solid var(--white);border-radius:2px;padding:1px}
  .battery-shape span{display:block;width:100%;height:100%;background:var(--white)}
  .nav-bar{height:44px;background:var(--bar);position:relative;display:flex;align-items:center;justify-content:center}
  .nav-title{color:var(--orange);font-size:18px;font-weight:500}
  .nav-back{position:absolute;left:12px;top:13px}
  .hero{position:relative;height:250px}
  .hero-backdrop{position:absolute;inset:0;background:radial-gradient(circle at 62% 45%,#d9545e 0,#c9677a 18%,#7d8fc6 48%,#6a83c4 100%)}
  .hero-shade{position:absolute;inset:0;background:linear-gradient(180deg,rgba(0,0,0,0) 60%,rgba(0,0,0,.25))}
  .settings{position:absolute;left:14px;top:12px}
  .avatar{position:absolute;left:137px;top:24px;width:140px;height:140px;border-radius:50%;border:4px solid var(--white);background:linear-gradient(135deg,#f2b7a6,#e6887d 45%,#3a2b2b 80%)}
  .profile-name{position:absolute;left:0;right:0;top:176px;text-align:center;color:var(--white);font-size:19px;font-weight:500}
  .round-btn{position:absolute;width:44px;height:44px;border-radius:50%;background:var(--bar);border:2px solid var(--white);display:flex;align-items:center;justify-content:center}
  .btn-wave{left:302px;top:36px}
  .btn-plug{left:70px;top:192px}
  .player-band{height:100px;background:var(--band);position:relative;display:flex;align-items:center;padding:0 14px;gap:14px}
  .controls{display:flex;gap:8px}
  .ctrl{width:36px;height:36px;border-radius:50%;border:2px solid var(--orange);display:flex;align-items:center;justify-content:center}
  .now-playing{flex:1}
  .np-label{color:var(--orange);font-size:14px;font-weight:600}
  .np-track{color:var(--yellow);font-size:11px;margin-top:4px}
  .progress{margin-top:8px;height:3px;background:#555;border-radius:2px}
  .progress span{display:block;width:72%;height:100%;background:var(--orange)}
  .lower{display:flex;height:322px}
  .side-panel{width:120px;background:linear-gradient(180deg,var(--panel-top),var(--panel-bottom));padding:12px 10px;display:flex;flex-direction:column;align-items:center}
  .playlist-head{display:flex;align-items:center;gap:6px;font-size:13px;font-weight:500;color:#222;align-self:flex-start}
  .menu-toggle{margin:14px 0 8px}
  .menu{list-style:none;display:flex;flex-direction:column;gap:16px;width:100%}
  .menu li{display:flex;align-items:center;gap:10px;font-size:12px;color:#222}
  .grid{flex:1;display:grid;grid-template-columns:repeat(3,88px);grid-auto-rows:88px;gap:8px;padding:10px}
  .track{position:relative;overflow:hidden}
  .track-art{position:absolute;inset:0}
  .track-meta{position:absolute;left:0;right:0;bottom:0;padding:3px 5px;background:linear-gradient(180deg,rgba(0,0,0,0),rgba(0,0,0,.55));color:var(--white)}
  .track-title{font-size:11px;font-weight:600}
  .track-plays{font-size:9px;color:var(--muted)}
</style>
</head>
<body>
<main class="screen">
  <div class="status-bar">
    <div class="status-left">
      <svg width="34" height="6" viewBox="0 0 34 6"><g fill="#fff"><circle cx="3" cy="3" r="2.6"/><circle cx="10" cy="3" r="2.6"/><circle cx="17" cy="3" r="2.6"/></g><g fill="none" stroke="#fff" stroke-width=".8"><circle cx="24" cy="3" r="2.3"/><circle cx="31" cy="3" r="2.3"/></g></svg>
      <span>KESTREL</span>
      <svg width="12" height="9" viewBox="0 0 12 9"><path d="M1 3.5a7 7 0 0 1 10 0M3 5.5a4 4 0 0 1 6 0" fill="none" stroke="#fff" stroke-width="1.3"/><circle cx="6" cy="7.6" r="1.1" fill="#fff"/></svg>
    </div>
    <span>4:21 PM</span>
    <div class="battery"><span>100%</span><div class="battery-shape"><span></span></div></div>
  </div>

  <header class="nav-bar">
    <svg class="nav-back" width="12" height="18" viewBox="0 0 12 18"><path d="M10 2 3 9l7 7" fill="none" stroke="var(--orange)" stroke-width="2.5"/></svg>
    <h1 class="nav-title">Profile</h1>
  </header>

  <section class="hero">
    <div class="hero-backdrop" role="img" aria-label="Blurred cover photo of the listener behind the profile"></div>
    <div class="hero-shade"></div>
    <svg class="settings" width="22" height="22" viewBox="0 0 24 24"><path fill="#fff" d="M19.4 13a7.5 7.5 0 0 0 0-2l2.1-1.6-2-3.5-2.5 1a7 7 0 0 0-1.7-1L15 3h-4l-.4 2.9a7 7 0 0 0-1.7 1l-2.5-1-2 3.5L6.6 11a7.5 7.5 0 0 0 0 2l-2.1 1.6 2 3.5 2.5-1a7 7 0 0 0 1.7 1L11 21h4l.4-2.9a7 7 0 0 0 1.7-1l2.5 1 2-3.5zM13 15.5a3.5 3.5 0 1 1 0-7 3.5 3.5 0 0 1 0 7z"/></svg>
    <div class="avatar" role="img" aria-label="Profile photo of Mara Quill wearing headphones"></div>
    <p class="profile-name">Mara Quill</p>
    <div class="round-btn btn-wave">
      <svg width="24" height="18" viewBox="0 0 24 18"><g fill="#fff"><rect x="1" y="7" width="3" height="6" rx="1"/><rect x="6" y="3" width="3" height="14" rx="1"/><rect x="11" y="0" width="3" height="18" rx="1"/><rect x="16" y="4" width="3" height="12" rx="1"/><rect x="21" y="7" width="2.5" height="6" rx="1"/></g></svg>
    </div>
    <div class="round-btn btn-plug">
      <svg width="22" height="12" viewBox="0 0 22 12"><rect x="0" y="1" width="14" height="10" rx="2" fill="#fff"/><rect x="14" y="3" width="7" height="6" fill="#fff"/></svg>
    </div>
  </section>

  <section class="player-band">
    <div class="controls">
      <div class="ctrl"><svg width="12" height="12" viewBox="0 0 12 12"><path d="M10 1 3 6l7 5z" fill="var(--orange)"/></svg></div>
      <div class="ctrl"><svg width="12" height="12" viewBox="0 0 12 12"><rect x="2" y="1" width="3" height="10" fill="var(--orange)"/><rect x="7" y="1" width="3" height="10" fill="var(--orange)"/></svg></div>
      <div class="ctrl"><svg width="12" height="12" viewBox="0 0 12 12"><path d="M2 1l7 5-7 5z" fill="var(--orange)"/></svg></div>
    </div>
    <div class="now-playing">
      <p class="np-label">Last Played</p>
      <p class="np-track">Only One – Mara Quill – ext.</p>
      <div class="progress"><span></span></div>
    </div>
    <svg width="30" height="26" viewBox="0 0 30 26"><g fill="var(--orange)"><rect x="0" y="10" width="4" height="16"/><rect x="6" y="4" width="4" height="22"/><rect x="12" y="0" width="4" height="26"/><rect x="18" y="6" width="4" height="20"/><rect x="24" y="12" width="4" height="14"/></g></svg>
  </section>

  <section class="lower">
    <aside class="side-panel">
      <div class="playlist-head">Playlist
        <svg width="10" height="7" viewBox="0 0 10 7"><path d="M1 1l4 4 4-4" fill="none" stroke="#444" stroke-width="1.6"/></svg>
      </div>
      <svg class="menu-toggle" width="16" height="9" viewBox="0 0 16 9"><path d="M1 1l7 6 7-6" fill="none" stroke="#777" stroke-width="2"/></svg>
      <ul class="menu">
        <li><svg width="26" height="26" viewBox="0 0 26 26"><g fill="#fff" stroke="#555" stroke-width="1"><circle cx="20" cy="5" r="3.5"/><circle cx="6" cy="13" r="3.5"/><circle cx="20" cy="21" r="3.5"/></g><path d="M9 11.5l8-5M9 14.5l8 5" stroke="#555" stroke-width="1.6"/></svg>Share</li>
        <li><svg width="26" height="24" viewBox="0 0 26 24"><path d="M13 22S2 15 2 8a5.5 5.5 0 0 1 11-1 5.5 5.5 0 0 1 11 1c0 7-11 14-11 14z" fill="#fff" stroke="#555" stroke-width="1"/></svg>Likes</li>
        <li><svg width="26" height="24" viewBox="0 0 26 24"><rect x="2" y="7" width="22" height="15" rx="2" fill="#fff" stroke="#555" stroke-width="1"/><path d="M9 7V3h8v4" fill="none" stroke="#555" stroke-width="1.6"/></svg>Groups</li>
        <li><svg width="26" height="24" viewBox="0 0 26 24"><circle cx="13" cy="7" r="5" fill="#fff" stroke="#555" stroke-width="1"/><path d="M3 23a10 9 0 0 1 20 0z" fill="#fff" stroke="#555" stroke-width="1"/></svg>Following</li>
      </ul>
    </aside>

    <div class="grid">
      <article class="track"><div class="track-art" role="img" aria-label="Cover art for Track 1" style="background:linear-gradient(135deg,#c86a4a,#e8b07a)"></div><div class="track-meta"><p class="track-title">Track 1</p><p class="track-plays">12 plays</p></div></article>
      <article class="track"><div class="track-art" role="img" aria-label="Cover art for Track 2" style="background:linear-gradient(135deg,#7a8fa8,#c9d2dc)"></div><div class="track-meta"><p class="track-title">Track 2</p><p class="track-plays">12 plays</p></div></article>
      <article class="track"><div class="track-art" role="img" aria-label="Cover art for Track 3" style="background:linear-gradient(135deg,#f0a090,#b83a4a)"></div><div class="track-meta"><p class="track-title">Track 3</p><p class="track-plays">12 plays</p></div></article>
      <article class="track"><div class="track-art" role="img" aria-label="Cover art for Track 4" style="background:linear-gradient(135deg,#d8408a,#6a2a5a)"></div><div class="track-meta"><p class="track-title">Track 4</p><p class="track-plays">12 plays</p></div></article>
      <article class="track"><div class="track-art" role="img" aria-label="Cover art for Track 5" style="background:linear-gradient(135deg,#e0a030,#7a8a3a)"></div><div class="track-meta"><p class="track-title">Track 5</p><p class="track-plays">12 plays</p></div></article>
      <article class="track"><div class="track-art" role="img" aria-label="Cover art for Track 6" style="background:linear-gradient(135deg,#4a5a9a,#d8a0b0)"></div><div class="track-meta"><p class="track-title">Track 6</p><p class="track-plays">12 plays</p></div></article>
      <article class="track"><div class="track-art" role="img" aria-label="Cover art for Track 7" style="background:linear-gradient(135deg,#4a5a6a,#9aa0a8)"></div><div class="track-meta"><p class="track-title">Track 7</p><p class="track-plays">12 plays</p></div></article>
      <article class="track"><div class="track-art" role="img" aria-label="Cover art for Track 8" style="background:linear-gradient(135deg,#e8e0d8,#6a6a6a)"></div><div class="track-meta"><p class="track-title">Track 8</p><p class="track-plays">12 plays</p></div></article>
      <article class="track"><div class="track-art" role="img" aria-label="Cover art for Track 9" style="background:linear-gradient(135deg,#5a2a3a,#d04a5a)"></div><div class="track-meta"><p class="track-title">Track 9</p><p class="track-plays">12 plays</p></div></article>
    </div>
  </section>
</main>
</body>
</html>
```